BirchLane Hotel
BUSINESS CARDS, LETTERHEAD, ENVELOPES, FAX COVER, EMAIL SIGNATURE, signage, car
BirchLane Hotel - Hospitality Industry
Creative Brief
Simple
DOHYUN KWAK
President & C.E.O
B2 Sora Bldg. 41 Namul-ro, Daeseong 10470
oliver@blhotelgroup.com
www.blhotelgroup.com
BirchLane Haeden: 18 Solbat-gil, Haeden 20815 BirchLane Orim: 57 Gaetmul-ro, Orim 30442

```html
<!DOCTYPE html>
<html lang="en">
<head>
<meta charset="utf-8">
<title>BirchLane Hotel Stationery</title>
<link href="https://fonts.googleapis.com/css2?family=Open+Sans:wght@400;600;700&display=swap" rel="stylesheet">
<style>
  :root {
    --green: #7cc41f;
    --green-dark: #1f4f27;
    --paper: #ffffff;
    --ink: #3d3d3d;
    --ink-soft: #8a8a8a;
    --card-text: #cfe3c9;
    --rule: #dcdcdc;
    --backdrop: #e6e8e4;
  }
  * { box-sizing: border-box; margin: 0; padding: 0; }
  html, body { width: 1200px; height: 750px; overflow: hidden; }
  body {
    position: relative;
    background: var(--backdrop);
    font-family: "Open Sans", Arial, sans-serif;
    color: var(--ink);
  }
  .sheet {
    position: absolute;
    background: var(--paper);
    box-shadow: 0 2px 8px rgba(0,0,0,.12);
    overflow: hidden;
  }
  .brand { display: flex; align-items: center; gap: 7px; }
  .brand-dot { width: 16px; height: 16px; border-radius: 50%; background: var(--green); flex: none; }
  .brand-name { font-weight: 700; color: var(--green-dark); font-size: 14px; white-space: nowrap; }
  .small { font-size: 7px; line-height: 1.55; color: var(--ink-soft); white-space: nowrap; }
  .small strong { color: var(--ink); font-weight: 600; }

  /* Letterhead */
  .letterhead { left: 72px; top: 72px; width: 480px; height: 619px; }
  .letterhead .brand { position: absolute; left: 22px; top: 44px; }
  .letterhead .sender { position: absolute; right: 24px; top: 30px; text-align: right; }
  .letterhead .header-rule { position: absolute; left: 22px; right: 24px; top: 94px; height: 1px; background: var(--rule); }
  .letterhead .branches { position: absolute; left: 22px; bottom: 36px; display: flex; gap: 40px; }
  .letterhead .footer-rule { position: absolute; left: 0; right: 0; bottom: 20px; height: 1px; background: var(--rule); }
  .letterhead .footer-band { position: absolute; left: 0; right: 0; bottom: 0; height: 14px; background: var(--green); }

  /* Business card back */
  .card-back { left: 569px; top: 72px; width: 194px; height: 115px; background: var(--green-dark); }
  .card-back .branches { position: absolute; left: 12px; top: 10px; }
  .card-back .branches p { font-size: 6px; line-height: 1.5; color: var(--card-text); white-space: nowrap; }
  .card-back .branches p strong { color: var(--paper); font-weight: 600; }
  .card-back .branches .gap { height: 6px; }
  .card-back .brand { position: absolute; right: 12px; bottom: 12px; }
  .card-back .brand-name { color: var(--paper); font-size: 10px; }
  .card-back .brand-dot { width: 11px; height: 11px; }

  /* Business card front */
  .card-front { left: 782px; top: 77px; width: 207px; height: 110px; }
  .card-front .person { position: absolute; right: 12px; top: 10px; text-align: right; }
  .card-front .person-name { font-size: 8px; font-weight: 700; color: var(--ink); letter-spacing: .3px; }
  .card-front .person-title { font-size: 6px; color: var(--ink-soft); }
  .card-front .brand { position: absolute; left: 12px; top: 36px; }
  .card-front .brand-name { font-size: 9px; }
  .card-front .brand-dot { width: 11px; height: 11px; }
  .card-front .contact { position: absolute; right: 12px; top: 52px; text-align: right; font-size: 5.5px; line-height: 1.5; color: var(--ink-soft); white-space: nowrap; }
  .card-front .band { position: absolute; left: 0; right: 0; bottom: 0; height: 5px; background: var(--green); }

  /* Envelope back */
  .envelope-back { left: 569px; top: 202px; width: 535px; height: 230px; }
  .envelope-back svg { position: absolute; left: 0; top: 0; }
  .envelope-back .web { position: absolute; left: 0; right: 0; top: 52px; text-align: center; font-size: 8px; color: var(--paper); font-weight: 600; letter-spacing: .4px; }

  /* Envelope front */
  .envelope-front { left: 569px; top: 451px; width: 535px; height: 233px; }
  .envelope-front .brand { position: absolute; left: 18px; top: 30px; }
  .envelope-front .return { position: absolute; left: 18px; bottom: 24px; }
  .envelope-front .band { position: absolute; left: 0; right: 0; bottom: 0; height: 10px; background: var(--green); }
</style>
</head>
<body>

  <section class="sheet letterhead">
    <div class="brand"><span class="brand-dot"></span><span class="brand-name">BirchLane Hotel</span></div>
    <div class="sender small">
      <p>B2 Sora Bldg. 41 Namul-ro,</p>
      <p>Daeseong 10470</p>
      <p>tel. 02-555-0172 fax 02-555-0173</p>
      <p>oliver@blhotelgroup.com</p>
    </div>
    <div class="header-rule"></div>
    <div class="branches">
      <div class="small">
        <p><strong>BirchLane Orim</strong></p>
        <p>57 Gaetmul-ro, Orim 30442</p>
        <p>Marrowbrook Country Club</p>
        <p>phone 063-555-0148</p>
      </div>
      <div class="small">
        <p><strong>BirchLane Haeden</strong></p>
        <p>18 Solbat-gil,</p>
        <p>Haeden 20815</p>
        <p>phone 054-555-0126</p>
      </div>
    </div>
    <div class="footer-rule"></div>
    <div class="footer-band"></div>
  </section>

  <section class="sheet card-back">
    <div class="branches">
      <p><strong>BirchLane Orim</strong></p>
      <p>57 Gaetmul-ro, Orim 30442</p>
      <p>tel 063-555-0148</p>
      <div class="gap"></div>
      <p><strong>BirchLane Haeden</strong></p>
      <p>18 Solbat-gil, Haeden 20815</p>
      <p>tel 054-555-0126</p>
    </div>
    <div class="brand"><span class="brand-dot"></span><span class="brand-name">BirchLane Hotel</span></div>
  </section>

  <section class="sheet card-front">
    <div class="person">
      <p class="person-name">DOHYUN KWAK</p>
      <p class="person-title">President &amp; C.E.O</p>
    </div>
    <div class="brand"><span class="brand-dot"></span><span class="brand-name">BirchLane Hotel</span></div>
    <div class="contact">
      <p>B2 Sora Bldg. 41 Namul-ro,</p>
      <p>Daeseong 10470</p>
      <p>T 02-555-0172</p>
      <p>M 010-5550-1934</p>
      <p>oliver@blhotelgroup.com</p>
      <p>www.blhotelgroup.com</p>
    </div>
    <div class="band"></div>
  </section>

  <section class="sheet envelope-back">
    <svg width="535" height="230" viewBox="0 0 535 230">
      <polygon points="0,0 535,0 535,6 267.5,138 0,6" fill="var(--green)"/>
    </svg>
    <p class="web">www.blhotelgroup.com</p>
  </section>

  <section class="sheet envelope-front">
    <div class="brand"><span class="brand-dot"></span><span class="brand-name">BirchLane Hotel</span></div>
    <div class="return small">
      <p>B2 Sora Bldg. 41 Namul-ro,</p>
      <p>Daeseong 10470 &nbsp; www.blhotelgroup.com</p>
    </div>
    <div class="band"></div>
  </section>

</body>
</html>
```